Transparent Real Estate Experience

Looking for an Image/Graphic for a postcard and brochure that communicates a complete transparent experience when selling a home.
The image is to convey "seeing through", hence transparent or transparency. NO Hourglasses or magnifying glasses. To me, those convey different messages - hour glass is "time" and magnifying is "making something small look bigger".

Ideally, a glass house with the words under the glass so the house is transparent to the words that are being communicated.

Those are:
transparency, honesty, communication, integrity, ethics, clarity, principles, knowledge, experience, trust, fairness, responsibility.

OR - using a "glass font" with those words in a mosaic order so the words are all transparent.

Professional Look - no cartoons...See samples - only thing I could find to provide a starting point. Thanks!
Updates

Need extra days to review

Target Market(s)

People selling their homes

Industry/Entity Type

Real Estate

Colors
0054AA
0677BA
7BADD7
CADEEF
E8F1F8

Requirements
Must have
• "Transparent" Look - "See-through"
Should not have
• Cartoons

```html
<!DOCTYPE html>
<html lang="en">
<head>
<meta charset="utf-8">
<title>Transparency – Values Word Mosaic</title>
<link rel="stylesheet" href="https://fonts.googleapis.com/css2?family=Montserrat:wght@200;300;600;800;900&display=swap">
<style>
  :root {
    --sky: #8fc6e6;
    --sky-glow: #d4e9f6;
    --glass-white: #ffffff;
    --glass-tint: #e8f1f8;
    --glass-edge: #cadeef;
    --wood-dark: #7a5a44;
    --wood-light: #a7836a;
    --stone: #8f8c86;
  }
  html, body {
    margin: 0;
    padding: 0;
    width: 1200px;
    height: 653px;
    overflow: hidden;
  }
  .canvas {
    position: relative;
    width: 1200px;
    height: 653px;
    background: radial-gradient(ellipse 520px 260px at 610px 150px, var(--sky-glow) 0%, var(--sky) 100%);
    font-family: "Montserrat", Arial, sans-serif;
  }
  .scene {
    position: absolute;
    inset: 0;
    width: 1200px;
    height: 653px;
  }
  .word { font-family: "Montserrat", Arial, sans-serif; }
  .word--thin { font-weight: 200; fill: var(--glass-white); }
  .word--light { font-weight: 300; fill: var(--glass-white); }
  .word--semibold { font-weight: 600; fill: var(--glass-white); }
  .word--bold { font-weight: 800; fill: var(--glass-white); }
  .word--glass {
    font-weight: 900;
    fill: url(#glassFill);
    filter: url(#glassEdge);
  }
</style>
</head>
<body>
<main class="canvas">
  <svg class="scene" viewBox="0 0 1200 653" xmlns="http://www.w3.org/2000/svg">
    <defs>
      <linearGradient id="houseTones" x1="0" y1="0" x2="1" y2="1">
        <stop offset="0" stop-color="var(--wood-light)"/>
        <stop offset="0.55" stop-color="var(--wood-dark)"/>
        <stop offset="1" stop-color="var(--stone)"/>
      </linearGradient>
      <linearGradient id="glassFill" x1="0" y1="0" x2="0" y2="1">
        <stop offset="0" stop-color="var(--glass-white)" stop-opacity="0.9"/>
        <stop offset="0.5" stop-color="var(--glass-tint)" stop-opacity="0.5"/>
        <stop offset="1" stop-color="var(--glass-edge)" stop-opacity="0.8"/>
      </linearGradient>
      <filter id="glassEdge" x="-5%" y="-10%" width="110%" height="125%">
        <feDropShadow dx="0" dy="1.5" stdDeviation="1.2" flood-color="#2d4a5e" flood-opacity="0.45"/>
      </filter>
    </defs>

    <rect class="house-photo" role="img"
          aria-label="Photograph of a modern two-storey glass and timber house with trees and landscaped garden on a platform"
          x="220" y="120" width="790" height="430" rx="18"
          fill="url(#houseTones)"/>

    <g class="word-mosaic">
      <text class="word word--thin" x="452" y="184" font-size="42" textLength="239" lengthAdjust="spacingAndGlyphs">KNOWLEDGE</text>
      <text class="word word--glass" x="324" y="245" font-size="76" textLength="299" lengthAdjust="spacingAndGlyphs">CLARITY</text>
      <text class="word word--bold" x="732" y="222" font-size="37" textLength="191" lengthAdjust="spacingAndGlyphs">FAIRNESS</text>
      <text class="word word--glass" x="642" y="279" font-size="70" textLength="372" lengthAdjust="spacingAndGlyphs">INTEGRITY</text>
      <text class="word word--light" x="317" y="281" font-size="34" textLength="195" lengthAdjust="spacingAndGlyphs">PRINCIPLES</text>
      <text class="word word--glass" x="160" y="366" font-size="108" textLength="911" lengthAdjust="spacingAndGlyphs">TRANSPARENCY</text>
      <text class="word word--bold" x="555" y="398" font-size="34" textLength="283" lengthAdjust="spacingAndGlyphs">COMMUNICATION</text>
      <text class="word word--light" x="317" y="433" font-size="38" textLength="314" lengthAdjust="spacingAndGlyphs">RESPONSABILITY</text>
      <text class="word word--glass" x="692" y="453" font-size="68" textLength="232" lengthAdjust="spacingAndGlyphs">TRUST</text>
      <text class="word word--semibold" x="384" y="474" font-size="51" textLength="168" lengthAdjust="spacingAndGlyphs">ETHICS</text>
      <text class="word word--light" x="620" y="488" font-size="38" textLength="228" lengthAdjust="spacingAndGlyphs">EXPERIENCE</text>
    </g>
  </svg>
</main>
</body>
</html>
```